Create a bold and border around my logo to make it pop and sign graphic design

I would like someone to create a sign graphic design so I can use on the side of my trucks and put on yard signs. I would to remove a lot of the white and add more of the orange and blue to give it more pop when cars drive past. I would like the services to be removed and for you to leave space for a mobile number that i would add later. I don’t want my logo changed at all. I just want colour and design to be added to the background so i can use it in signage. Same colour as on the sign

```html
<!DOCTYPE html>
<html lang="en">
<head>
<meta charset="utf-8">
<title>Branchworthy Sign</title>
<link rel="stylesheet" href="https://fonts.googleapis.com/css2?family=Montserrat:wght@700;800&display=swap">
<style>
  :root {
    --backdrop: #cbcbcb;
    --brand-orange: #f07622;
    --brand-navy: #223e7c;
    --navy-soft: #5a74ad;
    --panel-white: #ffffff;
  }
  html, body {
    margin: 0;
    padding: 0;
    width: 1200px;
    height: 1200px;
    overflow: hidden;
    background: var(--backdrop);
  }
  .sign-canvas {
    display: block;
    width: 1200px;
    height: 1200px;
  }
  .brand-name {
    font-family: 'Montserrat', sans-serif;
    font-weight: 700;
    font-size: 96px;
    fill: var(--brand-navy);
  }
  .call-label {
    font-family: 'Montserrat', sans-serif;
    font-weight: 700;
    font-size: 76px;
    fill: var(--panel-white);
  }
  .phone-number {
    font-family: 'Montserrat', sans-serif;
    font-weight: 800;
    font-size: 138px;
    fill: var(--panel-white);
  }
</style>
</head>
<body>
<svg class="sign-canvas" viewBox="0 0 1200 1200" xmlns="http://www.w3.org/2000/svg">
  <defs>
    <radialGradient id="flourish-left-tone" cx="0.35" cy="0.35" r="0.8">
      <stop offset="0" stop-color="var(--navy-soft)"/>
      <stop offset="1" stop-color="var(--brand-navy)"/>
    </radialGradient>
    <radialGradient id="flourish-right-tone" cx="0.65" cy="0.35" r="0.8">
      <stop offset="0" stop-color="var(--navy-soft)"/>
      <stop offset="1" stop-color="var(--brand-navy)"/>
    </radialGradient>
    <clipPath id="inner-frame-clip">
      <rect x="123" y="290" width="955" height="620" rx="28"/>
    </clipPath>
  </defs>

  <!-- sign frame -->
  <rect class="sign-border" x="98" y="264" width="1003" height="671" fill="var(--brand-orange)"/>
  <rect class="sign-inner-frame" x="123" y="290" width="955" height="620" rx="28" fill="var(--brand-navy)"/>
  <rect class="sign-panel" x="127" y="297" width="947" height="417" fill="var(--panel-white)"/>

  <!-- corner flourishes -->
  <g clip-path="url(#inner-frame-clip)">
    <rect class="corner-flourish corner-flourish--left" role="img" aria-label="Navy swirl ornament in the top left corner"
          x="123" y="290" width="203" height="250" rx="40" fill="url(#flourish-left-tone)"/>
    <rect class="corner-flourish corner-flourish--right" role="img" aria-label="Navy swirl ornament in the top right corner"
          x="875" y="290" width="203" height="250" rx="40" fill="url(#flourish-right-tone)"/>
  </g>

  <!-- brand mark -->
  <circle class="brand-dot" cx="598" cy="431" r="104" fill="var(--brand-orange)"/>
  <text class="brand-name" x="602" y="629" text-anchor="middle" textLength="900" lengthAdjust="spacingAndGlyphs">BRANCHWORTHY</text>

  <!-- contact band -->
  <rect class="call-pill" x="508" y="673" width="185" height="77" rx="38.5" fill="var(--brand-orange)"/>
  <text class="call-label" x="601" y="739" text-anchor="middle">Call</text>
  <text class="phone-number" x="602" y="879" text-anchor="middle" textLength="900" lengthAdjust="spacingAndGlyphs">123 456 7890</text>
</svg>
</body>
</html>
```